Local Horticulturalist needs Business card design

Meridale Gardening would like to update our existing business card and utilize our new logo (design attached)....we specialize in getting the best out of our customers yard with professional maintenance programs, expert pruning and hedging and garden restorations.
Utilizing colors from attached logo I would like a design that implies professionalism and if possible our businesses love of restoration through plants.
I also sometimes write down for my customers a start date and price on the back of my current card
Target Market(s)
Home owners
Contractors
Industry/Entity Type
Gardener
Contact Information for Business Card
Trevor Kalbrook | Horticulturalist
ph: 0452739186
meridalegard@fernpost.com
www.meridalegardening.com.au
Requirements
Must have
- crucial information easy to read
- incorporate current logo
- Horticulturalist listed preferably near name
Nice to have
- currently I write a job start date and price on the back of my current card so something that integrates this would be beneficial
Should not have
- be pretty or flowerey
- be too white or basic

```html
<!DOCTYPE html>
<html lang="en">
<head>
<meta charset="utf-8">
<title>Meridale Gardening – Business Card</title>
<link rel="stylesheet" href="https://fonts.googleapis.com/css2?family=Open+Sans:wght@300;400;700&display=swap">
<style>
  :root {
    --page-bg: #ece9e3;
    --leaf-green: #6fbf2c;
    --leaf-green-light: #93d451;
    --olive: #7d7648;
    --earth-brown: #6e5f45;
    --sand: #e9e3d4;
    --paper: #ffffff;
    --rule-line: #dcd6c8;
    --card-shadow: 0 14px 34px rgba(60, 50, 30, 0.22);
  }
  * { margin: 0; padding: 0; box-sizing: border-box; }
  html, body {
    width: 1200px;
    height: 1000px;
    overflow: hidden;
    background: var(--page-bg);
    font-family: "Open Sans", Arial, sans-serif;
  }
  .card {
    position: absolute;
    left: 220px;
    width: 760px;
    height: 434px;
    overflow: hidden;
    border-radius: 4px;
    box-shadow: var(--card-shadow);
  }
  .card-front { top: 38px; }
  .card-back { top: 528px; background: var(--paper); }
  .card-art {
    position: absolute;
    inset: 0;
    width: 100%;
    height: 100%;
  }

  /* Front */
  .brand {
    position: absolute;
    display: flex;
    align-items: center;
    gap: 14px;
  }
  .brand-dot {
    width: 42px;
    height: 42px;
    border-radius: 50%;
    flex: none;
  }
  .brand-name {
    font-weight: 700;
    font-size: 34px;
    line-height: 1;
    letter-spacing: 0.2px;
  }
  .brand-tagline {
    font-weight: 400;
    font-size: 15px;
    letter-spacing: 1.6px;
    margin-top: 5px;
  }
  .card-front .brand { left: 60px; top: 52px; color: var(--paper); }
  .card-front .brand-dot { background: var(--paper); }

  .person {
    position: absolute;
    left: 60px;
    top: 160px;
    color: var(--paper);
  }
  .person-name { font-weight: 700; font-size: 24px; }
  .person-role { font-weight: 300; font-size: 24px; margin-top: 2px; }

  .contact-list {
    position: absolute;
    left: 360px;
    top: 250px;
    list-style: none;
    color: var(--paper);
    font-size: 20px;
    font-weight: 400;
  }
  .contact-list li {
    display: flex;
    align-items: center;
    gap: 14px;
    height: 40px;
  }
  .contact-icon { width: 22px; height: 22px; flex: none; }
  .contact-web { padding-left: 36px; }

  /* Back */
  .card-back .brand { left: 100px; top: 150px; color: var(--leaf-green); }
  .card-back .brand-name { font-size: 38px; }
  .card-back .brand-tagline { color: var(--earth-brown); }
  .card-back .brand-dot { background: var(--earth-brown); }
  .write-in {
    position: absolute;
    left: 30px;
    width: 470px;
    height: 0;
    border-top: 1.5px solid var(--rule-line);
  }
  .write-in-date { top: 300px; }
  .write-in-price { top: 370px; }
</style>
</head>
<body>

<section class="card card-front" aria-label="Business card front">
  <svg class="card-art" viewBox="0 0 760 434" preserveAspectRatio="none" aria-hidden="true">
    <defs>
      <linearGradient id="front-green" x1="0" y1="0" x2="1" y2="1">
        <stop offset="0" stop-color="#7cc935"/>
        <stop offset="0.6" stop-color="#6bb928"/>
        <stop offset="1" stop-color="#86cc40"/>
      </linearGradient>
      <linearGradient id="front-olive" x1="0" y1="0" x2="1" y2="0">
        <stop offset="0" stop-color="#8a8a4c" stop-opacity="0.55"/>
        <stop offset="1" stop-color="#776f45" stop-opacity="0.95"/>
      </linearGradient>
    </defs>
    <rect width="760" height="434" fill="url(#front-green)"/>
    <path d="M280 0 C 400 120 360 300 450 434 L760 434 L760 0 Z" fill="#9ad85a" opacity="0.28"/>
    <path d="M440 0 C 540 120 500 300 580 434 L760 434 L760 0 Z" fill="url(#front-olive)"/>
    <path d="M560 0 C 625 110 600 300 650 434 L695 434 C 648 300 672 110 612 0 Z" fill="#8fd24a"/>
    <path d="M690 0 C 730 120 720 300 760 380 L760 0 Z" fill="#94d454" opacity="0.8"/>
  </svg>

  <div class="brand">
    <span class="brand-dot"></span>
    <div>
      <div class="brand-name">Meridale Gardening</div>
      <div class="brand-tagline">Garden Restorations &amp; Maintenance</div>
    </div>
  </div>

  <div class="person">
    <div class="person-name">Trevor Kalbrook</div>
    <div class="person-role">Horticulturalist</div>
  </div>

  <ul class="contact-list">
    <li>
      <svg class="contact-icon" viewBox="0 0 24 24" aria-hidden="true">
        <path d="M6.6 10.8a15 15 0 0 0 6.6 6.6l2.2-2.2a1 1 0 0 1 1-.25 11.4 11.4 0 0 0 3.6.6 1 1 0 0 1 1 1V20a1 1 0 0 1-1 1A17 17 0 0 1 3 4a1 1 0 0 1 1-1h3.5a1 1 0 0 1 1 1c0 1.25.2 2.45.6 3.6a1 1 0 0 1-.25 1z" fill="#fff"/>
      </svg>
      <span>0452739186</span>
    </li>
    <li>
      <svg class="contact-icon" viewBox="0 0 24 24" aria-hidden="true">
        <rect x="2.5" y="5" width="19" height="14" rx="1" fill="none" stroke="#fff" stroke-width="1.8"/>
        <path d="M3 6l9 7 9-7" fill="none" stroke="#fff" stroke-width="1.8"/>
      </svg>
      <span>meridalegard@fernpost.com</span>
    </li>
    <li class="contact-web">www.meridalegardening.com.au</li>
  </ul>
</section>

<section class="card card-back" aria-label="Business card back">
  <svg class="card-art" viewBox="0 0 760 434" preserveAspectRatio="none" aria-hidden="true">
    <defs>
      <linearGradient id="back-wash" x1="0" y1="0" x2="1" y2="1">
        <stop offset="0" stop-color="#ffffff" stop-opacity="0"/>
        <stop offset="0.35" stop-color="#ece6d6"/>
        <stop offset="0.75" stop-color="#cfc5ab"/>
        <stop offset="1" stop-color="#d8eeb2"/>
      </linearGradient>
      <linearGradient id="back-stripe" x1="0" y1="0" x2="0" y2="1">
        <stop offset="0" stop-color="#a59a7e"/>
        <stop offset="1" stop-color="#b9d58a"/>
      </linearGradient>
    </defs>
    <rect width="760" height="434" fill="#ffffff"/>
    <path d="M380 0 C 450 150 420 320 500 434 L760 434 L760 0 Z" fill="url(#back-wash)"/>
    <path d="M640 150 C 605 260 630 360 700 434 L760 434 L760 170 Z" fill="url(#back-stripe)" opacity="0.85"/>
    <path d="M600 130 C 545 250 575 370 660 440" fill="none" stroke="#ffffff" stroke-width="34"/>
    <path d="M690 400 L760 330 L760 434 L660 434 Z" fill="#c8e69a" opacity="0.7"/>
  </svg>

  <div class="brand">
    <div>
      <div class="brand-name">Meridale Gardening</div>
      <div class="brand-tagline">Garden Restorations &amp; Maintenance</div>
    </div>
    <span class="brand-dot"></span>
  </div>

  <div class="write-in write-in-date"></div>
  <div class="write-in write-in-price"></div>
</section>

</body>
</html>
```